Marlows welding and seed cleaning Business cards

Jakes welding and seed cleaningWe clean wheat seed on farm with portable cleaners so the farmers have pure wheat seed to plant back for the next crop. We are certified to clean foundation, registered, and certified seed wheat. Our cleaners being portable make it easier for the farmers because we do it right on there farm so they don't have to haul it all to townWhen there is no wheat to clean we weld in the winter. We improve, add onto, and build new corrals. We also build sheds, cattle shelters, and wind breaks. Other welding is welcomed
Updates

Project Deadline Extended
Reason: I need to extend the deadline because I've been busy and not had my game together. I need more time figure out what I want yet

Industry/Entity Type

Agriculture

Contact Information for Business Card

Just "marlows welding and seed cleaning" on front and other info on the back
On the back side I would like to have my address.
Dalton Pruett
48392 W COUNTY RD 417
ISABELLA OK 73019
Phone #5804913062

Font styles to use
Sans Serif

Requirements
Must have
• list we are certified to clean foundation, registered, and certified wheat
• State that they are portable cleaners
• For the welding part list, add on to, improve on, and repair existing corrals and new corrals and other welding welcomed
Nice to have
• A wheat field with some metal corrals on the side with a nice classic looking barn for a background. Maybe some cattle in the corrals
• A nice looking farm yard would be good too

```html
<!DOCTYPE html>
<html lang="en">
<head>
<meta charset="UTF-8">
<title>Marlows Welding and Seed Cleaning – Business Card</title>
<link rel="stylesheet" href="https://fonts.googleapis.com/css2?family=Open+Sans:wght@400&family=Montserrat:wght@400;700;800&family=Roboto+Condensed:wght@700&display=swap">
<style>
  :root {
    --page: #ffffff;
    --ink: #000000;
    --paper: #ffffff;
    --accent-yellow: #f5e400;
    --brown-deep: #2a1408;
    --brown-mid: #6a3e1e;
    --brown-glow: #9a6a3e;
    --welding-top: #231a14;
    --welding-bottom: #4a3020;
    --wheat-top: #b8701e;
    --wheat-bottom: #a0742c;
  }
  * { margin: 0; padding: 0; box-sizing: border-box; }
  html, body {
    width: 1200px; height: 1000px; overflow: hidden;
    background: var(--page);
  }
  .canvas { position: relative; width: 1200px; height: 1000px; }

  /* Front */
  .card-front {
    position: absolute; left: 178px; top: 102px;
    width: 840px; height: 381px; overflow: hidden;
  }
  .photo-welding {
    position: absolute; left: 0; top: 0; width: 422px; height: 100%;
    background: linear-gradient(180deg, var(--welding-top) 0%, var(--welding-bottom) 100%);
  }
  .photo-wheat {
    position: absolute; left: 422px; top: 0; width: 418px; height: 100%;
    background: linear-gradient(180deg, var(--wheat-top) 0%, var(--wheat-bottom) 100%);
  }
  .brand-pill {
    position: absolute; left: 47px; top: 308px;
    width: 740px; height: 49px; border-radius: 25px;
    background: var(--ink); color: var(--paper);
    font-family: "Open Sans", sans-serif; font-weight: 400;
    font-size: 38px; line-height: 49px; text-align: center;
    letter-spacing: -0.4px; white-space: nowrap;
  }

  /* Back */
  .card-back {
    position: absolute; left: 176px; top: 515px;
    width: 838px; height: 367px; overflow: hidden;
    background:
      radial-gradient(ellipse at 48% 45%, var(--brown-glow) 0%, var(--brown-mid) 35%, transparent 75%),
      linear-gradient(180deg, #3a1e0c 0%, var(--brown-mid) 50%, var(--brown-deep) 100%);
  }
  .back-heading {
    position: absolute; left: 24px; top: 11px; white-space: nowrap;
    font-family: "Montserrat", sans-serif; font-weight: 800;
    font-size: 28px; color: var(--accent-yellow); letter-spacing: 3px;
  }
  .service-list {
    position: absolute; left: 32px; top: 53px; list-style: none;
    font-family: "Montserrat", sans-serif; font-weight: 400;
    font-size: 16.5px; color: var(--paper); line-height: 19px;
    letter-spacing: 2.4px; white-space: nowrap;
  }
  .service-list li { position: relative; padding-left: 16px; margin-bottom: 17px; }
  .service-list li::before { content: "*"; position: absolute; left: 0; top: 0; letter-spacing: 0; }
  .contact-strip { position: absolute; left: 0; top: 300px; width: 838px; height: 67px; }
  .contact-strip svg { position: absolute; left: 0; top: 0; }
  .name-tag {
    position: absolute; left: 2px; top: 18px; width: 240px; height: 48px;
    color: var(--paper); white-space: nowrap;
    font-family: "Open Sans", sans-serif; font-size: 31px; line-height: 48px;
    padding-left: 10px;
  }
  .address {
    position: absolute; left: 249px; top: 16px; width: 590px;
    font-family: "Roboto Condensed", sans-serif; font-weight: 700;
    font-size: 22.5px; color: var(--ink); text-align: center; white-space: nowrap;
    letter-spacing: 0.4px;
  }
  .phone {
    position: absolute; left: 249px; top: 41px; width: 590px;
    font-family: "Montserrat", sans-serif; font-weight: 800;
    font-size: 22px; line-height: 26px; color: var(--ink); text-align: center;
    letter-spacing: 6px; white-space: nowrap;
  }
</style>
</head>
<body>
<main class="canvas">
  <section class="card-front">
    <div class="photo-welding" role="img" aria-label="Photo of a welding torch throwing sparks in a workshop"></div>
    <div class="photo-wheat" role="img" aria-label="Photo of a golden wheat field under a sunset sky"></div>
    <div class="brand-pill">Marlows Welding And Seed Cleaning</div>
  </section>

  <section class="card-back">
    <h2 class="back-heading">At Marlows welding and seed cleaning...</h2>
    <ul class="service-list">
      <li>We use portable cleaners to clean your wheat seed &nbsp;so that you are<br>ready to plant the pure wheat seed for the next crop.</li>
      <li>You can get the cleaning done on your farms instead of hauling<br>it over to town.</li>
      <li>We are registered and certified professionals.</li>
      <li>&nbsp;We improve and build new corrals in winters.</li>
      <li>&nbsp;We can help you build sheds, cattle shelters, wind breaks, etc.</li>
      <li>&nbsp;Other welding jobs are also welcomed.</li>
    </ul>
    <div class="contact-strip">
      <svg width="838" height="67" viewBox="0 0 838 67" aria-hidden="true">
        <polygon fill="#ffffff" points="0,8 60,6 110,2 150,10 230,5 300,12 380,7 470,11 560,4 620,9 700,6 760,12 838,10 838,67 0,67"/>
        <polygon fill="#000000" points="2,18 232,18 248,42 232,66 2,66"/>
      </svg>
      <div class="name-tag">Dalton Pruett</div>
      <div class="address">ADDRESS: 48392 W COUNTY RD 417, ISABELLA, OK 73019</div>
      <div class="phone">PHONE # 5804913062</div>
    </div>
  </section>
</main>
</body>
</html>
```